3.5" x 11" Door Hanger Design - Residential Roofing Company

We are looking for a double-sided door hanger that we can hang on the doors of prospects. This door hanger would have some brief information about our company, a phone number, website, and then the services that we offer. I don't know that it will have enough room for a lot of pictures, but feel free to use those from the marketing brochure if you think it'll work and I can get you the original as needed.
I have uploaded our certifications, logo, and then our current marketing brochure. The design should be cohesive with our marketing brochure, but doesn't have to match it perfectly.
Lastly, attached is the template that we are planning to print off of. This has a tear off portion at the bottom for a business card for a sales rep. The size of the overall door hanger will be 3.5" x 11", with the bottom 2.5" being the tear off business card with the salesman's information. I'll get you the sales reps information during the final design phase, but we will need name, title, phone number, email, business address, business website, list of services, and then the words "AZ ROC 562071" all on that small portion as well so if they tear it off they still have all the info.

```html
<!DOCTYPE html>
<html lang="en">
<head>
<meta charset="utf-8">
<title>Juniper Peak Roofing – Door Hanger</title>
<link href="https://fonts.googleapis.com/css2?family=Arimo:wght@400&family=Arvo:ital,wght@0,400;0,700;1,400&family=Roboto:ital,wght@0,700;1,400&display=swap" rel="stylesheet">
<style>
  :root{
    --orange:#e1581f;
    --ink:#1d1d1d;
    --white:#ffffff;
    --stage:#6e6e6e;
    --muted:#555555;
    --badge:#cfcfcf;
  }
  *{box-sizing:border-box;margin:0;padding:0}
  html,body{width:835px;height:1200px;overflow:hidden}
  body{background:var(--stage);position:relative;font-family:"Arimo",sans-serif}
  .hanger{position:absolute;width:334px;height:1001px;overflow:hidden;box-shadow:0 2px 6px rgba(0,0,0,.35)}
  .hanger--front{left:73px;top:75px;background:var(--ink)}
  .hanger--back{left:445px;top:72px;background:var(--ink)}
  .hanger svg.art{position:absolute;left:0;top:0}
  .txt{position:absolute;left:0;width:100%;text-align:center;white-space:nowrap}
  .brand{font-family:"Arvo",serif;font-weight:700;font-size:23px;line-height:1}
  .brand--dark{color:var(--ink)}
  .brand--light{color:var(--white)}
  .headline{font-family:"Arvo",serif;font-weight:700;font-size:26.5px;line-height:26px;color:var(--orange)}
  .headline--front{font-size:29px;line-height:27px}
  .headline .lead{color:var(--white)}
  .tagline{font-family:"Roboto",sans-serif;font-style:italic;font-weight:400;font-size:27px;line-height:1;color:var(--white)}
  .rule{position:absolute;left:50%;width:22px;height:1px;margin-left:-11px;background:var(--orange)}
  .rule--light{background:#cfcfcf;width:30px;margin-left:-15px}
  .call{font-family:"Arvo",serif;font-size:17px;line-height:1;color:var(--white)}
  .phone{font-family:"Roboto",sans-serif;font-weight:700;font-size:27px;line-height:1;color:var(--orange)}
  .web-button{position:absolute;left:58px;top:758px;width:216px;height:28px;border-radius:14px;background:var(--orange);color:var(--white);font-family:"Arvo",serif;font-weight:700;font-size:10px;display:flex;align-items:center;justify-content:center;letter-spacing:.2px}
  .card-brand{position:absolute;left:0;top:913px;width:176px;text-align:center;font-family:"Arvo",serif;font-weight:700;font-size:12px;color:var(--ink)}
  .card-divider{position:absolute;left:176px;top:864px;width:1px;height:89px;background:#444}
  .card-info{position:absolute;left:185px;top:862px;font-size:7.6px;line-height:9.6px;color:#333}
  .card-info .rep{font-size:11.5px;line-height:13px;color:var(--orange);font-weight:400}
  .card-info .role{color:var(--muted);margin-bottom:2px}
  .card-info .gap{height:5px}
  .card-info .line{display:flex;align-items:center;gap:4px}
  .card-info svg{flex:none}
  .service-label{position:absolute;top:592px;font-family:"Arvo",serif;font-weight:700;font-size:7px;color:var(--white);transform:translateX(-50%);white-space:nowrap}
  .services-title{font-size:10px;color:var(--white)}
  .services-list{font-size:9.5px;color:var(--orange)}
</style>
</head>
<body>

<section class="hanger hanger--front">
  <svg class="art" width="334" height="1001" viewBox="0 0 334 1001">
    <defs>
      <linearGradient id="frontPhotoTone" x1="0" y1="0" x2="0" y2="1">
        <stop offset="0" stop-color="#8a90a2"/>
        <stop offset=".45" stop-color="#a9adb9"/>
        <stop offset=".62" stop-color="#8d8a84"/>
        <stop offset="1" stop-color="#9a9186"/>
      </linearGradient>
    </defs>
    <rect x="0" y="0" width="334" height="620" fill="url(#frontPhotoTone)" role="img" aria-label="Photo of a stone and siding home with a tile roof under a cloudy sky"/>
    <circle cx="167" cy="136" r="56" fill="var(--white)"/>
    <polyline points="0,566 81,527 122,546" fill="none" stroke="var(--orange)" stroke-width="6"/>
    <polyline points="0,574 81,535 122,554" fill="none" stroke="var(--white)" stroke-width="4"/>
    <polygon points="0,589 255,479 334,513 334,814 0,814" fill="var(--ink)"/>
    <polyline points="0,577 255,467 334,501" fill="none" stroke="var(--orange)" stroke-width="8"/>
    <polyline points="0,586 255,476 334,510" fill="none" stroke="var(--white)" stroke-width="4"/>
    <rect x="0" y="814" width="334" height="187" fill="var(--white)"/>
  </svg>

  <div class="txt brand brand--dark" style="top:286px">Juniper Peak Roofing</div>

  <div class="txt headline headline--front" style="top:576px"><span class="lead">INSTALLING</span><br>QUALITY ROOFS<br>ACROSS ARIZONA</div>
  <div class="rule" style="top:674px"></div>
  <div class="txt call" style="top:690px">Call Now</div>
  <div class="txt phone" style="top:712px">(928) 555 0147</div>
  <div class="web-button">WWW.JUNIPERPEAK-ROOFING.COM</div>

  <div class="card-brand">Juniper Peak Roofing</div>
  <div class="card-divider"></div>
  <div class="card-info">
    <div class="rep">Dale Moreno</div>
    <div class="role">President</div>
    <div>AZ ROC 562071</div>
    <div class="gap"></div>
    <div>412 W Pine Ave</div>
    <div>Prescott AZ 86301</div>
    <div class="gap"></div>
    <div class="line">
      <svg width="6" height="6" viewBox="0 0 10 10"><path d="M2 0.5 L4 2.8 L3 4 Q4.5 6 6 7 L7.2 6 L9.5 8 L8 9.5 Q3.5 9 0.5 2 Z" fill="var(--orange)"/></svg>
      <span>(928) 555-0147</span>
    </div>
    <div class="line">
      <svg width="6" height="6" viewBox="0 0 10 10"><rect x="0" y="2" width="10" height="6.5" fill="var(--orange)"/><polyline points="0,2 5,6 10,2" fill="none" stroke="var(--white)" stroke-width="1"/></svg>
      <span>info@juniperpeak-roofing.com</span>
    </div>
    <div class="line">
      <svg width="6" height="6" viewBox="0 0 10 10"><circle cx="5" cy="5" r="4.3" fill="none" stroke="var(--orange)" stroke-width="1.3"/><path d="M1 5 H9 M5 1 Q2.5 5 5 9 M5 1 Q7.5 5 5 9" fill="none" stroke="var(--orange)" stroke-width=".9"/></svg>
      <span>www.juniperpeak-roofing.com</span>
    </div>
  </div>
</section>

<section class="hanger hanger--back">
  <svg class="art" width="334" height="1001" viewBox="0 0 334 1001">
    <defs>
      <linearGradient id="tileTone" x1="0" y1="0" x2="1" y2="1"><stop offset="0" stop-color="#e87040"/><stop offset="1" stop-color="#b9461c"/></linearGradient>
      <linearGradient id="lowSlopeTone" x1="0" y1="0" x2="0" y2="1"><stop offset="0" stop-color="#b7a993"/><stop offset=".45" stop-color="#6d6a66"/><stop offset="1" stop-color="#9ba2aa"/></linearGradient>
      <linearGradient id="metalTone" x1="0" y1="0" x2="0" y2="1"><stop offset="0" stop-color="#6f7780"/><stop offset="1" stop-color="#3b3d40"/></linearGradient>
      <linearGradient id="shingleTone" x1="0" y1="0" x2="1" y2="1"><stop offset="0" stop-color="#6d6b73"/><stop offset="1" stop-color="#47464c"/></linearGradient>
      <linearGradient id="backPhotoTone" x1="0" y1="0" x2="1" y2="1">
        <stop offset="0" stop-color="#6c6a5c"/>
        <stop offset=".4" stop-color="#8f8587"/>
        <stop offset="1" stop-color="#a19598"/>
      </linearGradient>
      <clipPath id="collageShape"><polygon points="18,581 18,535 168,470 320,535 320,581"/></clipPath>
    </defs>

    <circle cx="167" cy="135" r="56" fill="var(--white)"/>

    <g clip-path="url(#collageShape)">
      <rect x="18" y="460" width="84" height="125" fill="url(#tileTone)" role="img" aria-label="Photo of clay tile roofing"/>
      <rect x="102" y="460" width="66" height="125" fill="url(#lowSlopeTone)" role="img" aria-label="Photo of a low slope roof at sunset"/>
      <rect x="168" y="460" width="67" height="125" fill="url(#metalTone)" role="img" aria-label="Photo of a metal roof"/>
      <rect x="235" y="460" width="85" height="125" fill="url(#shingleTone)" role="img" aria-label="Photo of an asphalt shingle roof"/>
    </g>
    <g stroke="var(--white)" stroke-width="2.5" fill="none">
      <polygon points="18,581 18,535 168,470 320,535 320,581"/>
      <line x1="102" y1="499" x2="102" y2="581"/>
      <line x1="168" y1="470" x2="168" y2="581"/>
      <line x1="235" y1="499" x2="235" y2="581"/>
    </g>
    <circle cx="98" cy="495" r="24" fill="var(--badge)" role="img" aria-label="Roofing manufacturer certification badge"/>
    <circle cx="243" cy="494" r="27" fill="var(--badge)" role="img" aria-label="Roofing manufacturer certification badge"/>

    <rect x="0" y="613" width="334" height="201" fill="url(#backPhotoTone)" role="img" aria-label="Aerial photo of a multi-tone concrete tile roof with a chimney"/>
    <polygon points="0,610 334,610 334,629 215,684 82,616 0,650" fill="var(--ink)"/>
    <polyline points="0,641 82,607 215,675" fill="none" stroke="var(--orange)" stroke-width="8"/>
    <polyline points="0,648 82,614 215,682" fill="none" stroke="var(--white)" stroke-width="4"/>
    <polyline points="215,681 334,741" fill="none" stroke="var(--white)" stroke-width="4"/>
    <polyline points="215,673 334,733" fill="none" stroke="var(--orange)" stroke-width="7"/>
    <polyline points="210,678 334,620" fill="none" stroke="var(--orange)" stroke-width="8"/>
    <polyline points="214,685 334,628" fill="none" stroke="var(--white)" stroke-width="4"/>
  </svg>

  <div class="txt brand brand--light" style="top:276px">Juniper Peak Roofing</div>

  <div class="txt headline" style="top:325px">QUALITY ROOFING</div>
  <div class="txt tagline" style="top:351px">YOU CAN TRUST</div>
  <div class="rule rule--light" style="top:388px"></div>
  <div class="txt call" style="top:398px">Call Now</div>
  <div class="txt phone" style="top:420px">(928) 555 0147</div>

  <div class="service-label" style="left:55px">TILE</div>
  <div class="service-label" style="left:131px">LOW SLOPE</div>
  <div class="service-label" style="left:197px">METAL</div>
  <div class="service-label" style="left:279px">SHINGLE</div>

  <div class="txt brand brand--light" style="top:908px">Juniper Peak Roofing</div>
  <div class="txt services-title" style="top:956px">Residential Roofing Services</div>
  <div class="txt services-list" style="top:970px">TILE - METAL - SHINGLE - LOW SLOPE</div>
</section>

</body>
</html>
```